Business Card Design for a Personal Trainer

I need a business card design for my job as a personal trainer. It should have a unique, modern and exclusive design. On the front there should be only my logo with my name and my job. 0163/2918374 Tobias Hellwig Lindenkopfweg 14 80921 Munich Germany The most important contact information is the web adress. it can be bigger than the rest, but its not necessary. The card should be 8,5cmx5,5cm big. Font: Roboto. Colors: black, white, gray, 56c1ff.

```html
<!DOCTYPE html>
<html lang="de">
<head>
<meta charset="utf-8">
<title>Tobias Hellwig – Visitenkarte</title>
<link href="https://fonts.googleapis.com/css2?family=Roboto:wght@300;400;500;700&display=swap" rel="stylesheet">
<style>
  :root {
    --page: #d6d6d8;
    --card: #0b0b0b;
    --band: #171717;
    --white: #ffffff;
    --soft: #e6e6e6;
    --ink: #1a1a1a;
  }
  * { margin: 0; padding: 0; box-sizing: border-box; }
  html, body { width: 1200px; height: 937px; overflow: hidden; }
  body {
    background: var(--page);
    font-family: "Roboto", sans-serif;
    color: var(--white);
    position: relative;
  }
  .card {
    position: absolute;
    top: 64px;
    width: 526px;
    height: 810px;
    background: var(--card);
    overflow: hidden;
  }
  .card--front { left: 68px; }
  .card--back { left: 610px; }

  /* front */
  .portrait {
    position: absolute;
    inset: 0;
    background:
      radial-gradient(ellipse 48% 62% at 50% 62%, #4a4a4a 0%, #2c2c2c 45%, #0b0b0b 80%),
      var(--card);
  }
  .brand-mark {
    position: absolute;
    left: 0; right: 0;
    top: 580px;
    display: flex;
    justify-content: center;
    align-items: center;
    gap: 12px;
    font-size: 34px;
    font-weight: 700;
    letter-spacing: 6px;
  }
  .brand-mark__square {
    width: 18px; height: 18px;
    background: var(--white);
  }
  .front-name {
    position: absolute;
    left: 0; right: 0;
    top: 658px;
    text-align: center;
    font-size: 35px;
    font-weight: 400;
    letter-spacing: 0.5px;
  }
  .front-role {
    position: absolute;
    left: 0; right: 0;
    top: 695px;
    display: flex;
    justify-content: center;
    align-items: center;
    gap: 8px;
    font-size: 14px;
    font-weight: 400;
    letter-spacing: 3.5px;
  }
  .front-role::before, .front-role::after {
    content: "";
    width: 38px;
    height: 1px;
    background: var(--white);
  }
  .front-web {
    position: absolute;
    left: 0; right: 0;
    top: 738px;
    height: 41px;
    background: var(--white);
    color: var(--ink);
    display: flex;
    align-items: center;
    justify-content: center;
    font-size: 18px;
    letter-spacing: 2px;
  }

  /* back */
  .back-mark {
    position: absolute;
    left: 0; right: 0;
    top: 196px;
    display: flex;
    justify-content: center;
    align-items: center;
    gap: 14px;
    font-size: 40px;
    font-weight: 700;
    letter-spacing: 7px;
  }
  .back-mark__square {
    width: 22px; height: 22px;
    background: var(--white);
  }
  .name-band {
    position: absolute;
    left: 0; right: 0;
    top: 418px;
    height: 56px;
    background: var(--band);
    display: flex;
    align-items: center;
    justify-content: center;
    font-size: 19px;
    font-weight: 700;
    letter-spacing: 3.5px;
  }
  .contact {
    position: absolute;
    left: 0; right: 0;
    display: flex;
    justify-content: center;
    gap: 14px;
    font-size: 18px;
    font-weight: 300;
    letter-spacing: 1.6px;
    line-height: 24px;
  }
  .contact svg { width: 16px; height: 16px; margin-top: 4px; fill: var(--white); flex: none; }
  .contact--phone { top: 522px; }
  .contact--mail { top: 570px; }
  .contact--address { top: 614px; }
  .contact--address .contact__text { text-align: center; }
  .back-web {
    position: absolute;
    left: 0; right: 0;
    top: 743px;
    text-align: center;
    font-size: 19px;
    font-weight: 700;
    letter-spacing: 3px;
  }
</style>
</head>
<body>
  <section class="card card--front">
    <div class="portrait" role="img" aria-label="Schwarz-weiß Porträt des Trainers mit verschränkten Armen vor schwarzem Hintergrund"></div>
    <div class="brand-mark"><span class="brand-mark__square"></span>HELLWIG</div>
    <h1 class="front-name">TOBIAS HELLWIG</h1>
    <p class="front-role">PERSONAL TRAINER</p>
    <p class="front-web">www.tobiashellwig.de</p>
  </section>

  <section class="card card--back">
    <div class="back-mark"><span class="back-mark__square"></span>HELLWIG</div>
    <h2 class="name-band">TOBIAS HELLWIG</h2>
    <p class="contact contact--phone">
      <svg viewBox="0 0 24 24" aria-hidden="true"><path d="M6.6 10.8a15.1 15.1 0 0 0 6.6 6.6l2.2-2.2c.3-.3.7-.4 1-.2 1.1.4 2.3.6 3.6.6.6 0 1 .4 1 1V20c0 .6-.4 1-1 1A17 17 0 0 1 3 4c0-.6.4-1 1-1h3.5c.6 0 1 .4 1 1 0 1.3.2 2.5.6 3.6.1.3 0 .7-.2 1z"/></svg>
      <span class="contact__text">0163/2918374</span>
    </p>
    <p class="contact contact--mail">
      <svg viewBox="0 0 24 24" aria-hidden="true"><path d="M2 5h20v14H2z M3.5 6.5 12 13l8.5-6.5" fill="none" stroke="#fff" stroke-width="0"/><path d="M2 5h20v1.2L12 13 2 6.2zM2 8l10 6.8L22 8v11H2z"/></svg>
      <span class="contact__text">t.hellwig@postfach.de</span>
    </p>
    <div class="contact contact--address">
      <svg viewBox="0 0 24 24" aria-hidden="true"><path d="M12 2a7 7 0 0 0-7 7c0 5.2 7 13 7 13s7-7.8 7-13a7 7 0 0 0-7-7zm0 2a5 5 0 0 1 5 5c0 3.4-3.6 8.3-5 10-1.4-1.7-5-6.6-5-10a5 5 0 0 1 5-5zm0 2.5a2.5 2.5 0 1 0 0 5 2.5 2.5 0 0 0 0-5z"/></svg>
      <p class="contact__text">Lindenkopfweg 14<br>80921 München</p>
    </div>
    <p class="back-web">www.tobiashellwig.de</p>
  </section>
</body>
</html>
```